Smart Coffee Shop Needs a Poster Design

New smart coffee shop called Brewlyn using touch screens as table tops. all information in attached file. the café is now open in a busy mall in Abu Dhabi.
We need creative design for 2 posters on two sides of a column. This is to attract the attention of people from a distance. We need it to be colorful and preferably in two languages: English and Arabic.
The dimensions are: 275 (H) x 75 (W) cm & 275 (H) x 87 (W) cm.
Catch phrase could be: The Smartest and Coolest Café on Earth. or something similar. Attached also is the hoarding poster.
Project Deadline Extended
Reason: Received 8 designs only. Still looking for more creative ideas. If we select your design, we will be providing more jobs (website, facebook, brochures, flyers, more posters etc..).
Industry/Entity Type
Coffee Shop
Look and feel
Each slider illustrates characteristics of the customer's brand and the style your logo design should communicate.

```html
<!DOCTYPE html>
<html lang="en">
<head>
<meta charset="utf-8">
<title>Brewlyn – Column Posters</title>
<link rel="stylesheet" href="https://fonts.googleapis.com/css2?family=Josefin+Sans:wght@600;700&display=swap">
<style>
  :root {
    --stage-top: #f2f3f7;
    --stage-bottom: #d9dcea;
    --space-purple: #6a2d78;
    --space-violet: #3a2a6c;
    --space-navy: #1b2052;
    --space-blue: #1f4f9a;
    --space-cyan: #2f8fc9;
    --ink-white: #ffffff;
    --label-grey: #5a5d68;
    --panel-tint: rgba(170, 150, 210, 0.18);
    --panel-edge: rgba(255, 255, 255, 0.25);
  }
  * { box-sizing: border-box; margin: 0; padding: 0; }
  html, body { width: 1200px; height: 1200px; overflow: hidden; }
  body {
    background: radial-gradient(ellipse at 50% 35%, var(--stage-top) 0%, var(--stage-bottom) 100%);
    font-family: "Josefin Sans", "Trebuchet MS", sans-serif;
    position: relative;
  }
  .poster {
    position: absolute;
    top: 142px;
    height: 856px;
    overflow: hidden;
    color: var(--ink-white);
    box-shadow: 4px 6px 14px rgba(40, 45, 70, 0.35);
  }
  .poster--narrow { left: 250px; width: 316px; }
  .poster--wide { left: 592px; width: 354px; }
  .poster__backdrop {
    position: absolute; inset: 0;
    background:
      radial-gradient(ellipse at 20% 8%, rgba(170, 70, 160, 0.55) 0%, transparent 45%),
      linear-gradient(180deg, var(--space-purple) 0%, var(--space-violet) 28%, var(--space-navy) 55%, var(--space-blue) 82%, var(--space-cyan) 100%);
  }
  .brand {
    position: absolute; left: 0; right: 0; top: 78px;
    display: flex; align-items: center; justify-content: center; gap: 10px;
    font-weight: 700; font-size: 40px; letter-spacing: 0.5px;
  }
  .brand__dot {
    width: 14px; height: 14px; border-radius: 50%;
    background: var(--ink-white);
  }
  .headline-panel {
    position: absolute; left: 47px; top: 208px; width: 220px; height: 299px;
    border: 2px solid var(--panel-edge);
    border-radius: 8px;
    background: var(--panel-tint);
    display: flex; align-items: center; justify-content: center;
    text-align: center;
  }
  .headline-panel__text {
    font-weight: 700; font-size: 31px; line-height: 43px; letter-spacing: 0.5px;
    padding-top: 6px;
  }
  .invite {
    position: absolute; left: 0; right: 0; text-align: center;
    font-weight: 700; text-transform: uppercase;
  }
  .poster--narrow .invite { top: 530px; font-size: 19px; line-height: 26px; }
  .invite__strong { font-size: 23px; }
  .table-shot {
    position: absolute;
    border-radius: 12px;
    background: linear-gradient(160deg, #5b5f6c 0%, #3c2c55 40%, #2b3a5a 70%, #9da3ad 100%);
    box-shadow: 0 0 14px 4px rgba(255, 255, 255, 0.55);
  }
  .poster--narrow .table-shot { left: 44px; top: 632px; width: 226px; height: 210px; }
  .poster--wide .table-shot { left: 44px; top: 598px; width: 266px; height: 228px; }
  .slanted {
    position: absolute; left: 0; top: 200px; width: 354px;
    transform: rotate(-9deg); transform-origin: 50% 50%;
    text-align: right; padding-right: 36px;
    font-weight: 700; text-transform: uppercase; line-height: 1;
  }
  .slanted__line { display: block; }
  .slanted__s { font-size: 38px; margin-bottom: 4px; }
  .slanted__m { font-size: 40px; margin-bottom: 4px; }
  .slanted__l { font-size: 30px; margin-bottom: 2px; }
  .slanted__xl { font-size: 74px; margin-bottom: -2px; }
  .slanted__small-lead { font-size: 30px; }
  .slanted__rule {
    display: block; height: 2px; background: var(--ink-white);
    margin: 12px -10px 10px 20px;
  }
  .slanted__invite { font-size: 15px; letter-spacing: 3px; line-height: 18px; text-align: left; padding-left: 52px; }
  .slanted__invite strong { letter-spacing: 1px; font-size: 16px; }
  .size-label {
    position: absolute; top: 1096px;
    font-family: "Josefin Sans", "Trebuchet MS", sans-serif;
    font-weight: 600; font-size: 26px; color: var(--label-grey); letter-spacing: 0.5px;
    transform: translateX(-50%); white-space: nowrap;
  }
</style>
</head>
<body>

  <section class="poster poster--narrow">
    <div class="poster__backdrop" role="img" aria-label="Starry outer-space background in purple, navy and blue with the Earth's glow at the bottom"></div>
    <div class="brand"><span class="brand__dot"></span>Brewlyn</div>
    <div class="headline-panel">
      <p class="headline-panel__text">THE<br>SMARTEST<br>AND<br>COOLEST<br>CAFÉ ON<br>EARTH</p>
    </div>
    <p class="invite">Come in and try<br>our interactive<br><span class="invite__strong">Smart tables</span></p>
    <div class="table-shot" role="img" aria-label="Photo of guests' hands using an interactive touch-screen table top"></div>
  </section>

  <section class="poster poster--wide">
    <div class="poster__backdrop" role="img" aria-label="Starry outer-space background in purple, navy and blue with the Earth's glow at the bottom"></div>
    <div class="brand"><span class="brand__dot"></span>Brewlyn</div>
    <div class="slanted">
      <span class="slanted__line slanted__s">The</span>
      <span class="slanted__line slanted__m">Smartest</span>
      <span class="slanted__line slanted__l">and Coolest</span>
      <span class="slanted__line slanted__xl">Café</span>
      <span class="slanted__line slanted__small-lead">on <span style="font-size:46px">Earth</span></span>
      <span class="slanted__rule"></span>
      <span class="slanted__line slanted__invite">Come in and try our<br><strong>Interactive smart tables</strong></span>
    </div>
    <div class="table-shot" role="img" aria-label="Photo of guests' hands using an interactive touch-screen table top"></div>
  </section>

  <p class="size-label" style="left:406px">85 cm x 230 cm</p>
  <p class="size-label" style="left:768px">95 cm x 230 cm</p>

</body>
</html>
```